New Infographic Design Project

Hi, I have another project to work on if you are interested. It is a horizontal style infographic with 6 steps. It should display the step Number (1-6), Title, and an Icon.

Step 1 - Strong Phone Interview
Step 2 - Pre-Employment
Step 3 - Prep & Do In-Person Interview
Step 4 - Second Interview
Step 5 - Reference Checks
Step 6 - Job Offer

More flexible on colors with this one, but keep it professional.

```html
<!DOCTYPE html>
<html lang="en">
<head>
<meta charset="utf-8">
<title>Hiring Process in Six Steps</title>
<link href="https://fonts.googleapis.com/css2?family=Oswald:wght@500&family=Montserrat:wght@700&display=swap" rel="stylesheet">
<style>
  :root {
    --teal: #0a9e9a;
    --blue: #3a6db5;
    --sky: #2f8fd0;
    --bg: #ffffff;
  }
  * { margin: 0; padding: 0; box-sizing: border-box; }
  html, body { width: 1200px; height: 512px; overflow: hidden; background: var(--bg); }
  .process { position: relative; width: 1200px; height: 512px; }
  .step-badge { position: absolute; top: 101px; width: 120px; height: 120px; margin-left: -60px; }
  .step-number {
    position: absolute; inset: 0; display: flex; align-items: center; justify-content: center;
    font-family: "Montserrat", sans-serif; font-weight: 700; font-size: 37px; color: var(--blue);
  }
  .connector { position: absolute; top: 212px; height: 60px; border-left: 1.5px dashed var(--teal); }
  .step-icon { position: absolute; top: 277px; height: 74px; }
  .step-icon svg { display: block; width: 100%; height: 100%; }
  .step-title {
    position: absolute; top: 357px; width: 220px; margin-left: -110px; text-align: center;
    font-family: "Oswald", sans-serif; font-weight: 500; font-size: 16px; line-height: 20px;
    color: var(--blue); white-space: nowrap;
  }
  .title-rule { position: absolute; height: 1px; background: var(--teal); }
  .rule-a { top: 386px; width: 109px; margin-left: -54px; }
  .rule-b { top: 390px; width: 62px; margin-left: -31px; }
  .rule-c { top: 394px; width: 36px; margin-left: -18px; }
  .divider { position: absolute; top: 280px; height: 111px; border-left: 1.5px solid var(--blue); }
</style>
</head>
<body>
<main class="process">
  <svg width="0" height="0" style="position:absolute">
    <defs>
      <linearGradient id="arc-grad" x1="0" y1="1" x2="1" y2="0">
        <stop offset="0" stop-color="#0a9e9a"/><stop offset="1" stop-color="#3a6db5"/>
      </linearGradient>
      <linearGradient id="icon-grad" x1="0" y1="0" x2="1" y2="1">
        <stop offset="0" stop-color="#0a9e9a"/><stop offset="1" stop-color="#3a6db5"/>
      </linearGradient>
      <linearGradient id="icon-grad-h" x1="0" y1="0" x2="1" y2="0">
        <stop offset="0" stop-color="#0a9e9a"/><stop offset="1" stop-color="#3a6db5"/>
      </linearGradient>
      <radialGradient id="disc-grad" cx="40%" cy="35%" r="70%">
        <stop offset="0" stop-color="#f6f6f8"/><stop offset="1" stop-color="#d9d9de"/>
      </radialGradient>
      <filter id="disc-shadow" x="-30%" y="-30%" width="160%" height="160%">
        <feDropShadow dx="1" dy="2" stdDeviation="1.6" flood-color="#000" flood-opacity=".35"/>
      </filter>
      <g id="badge">
        <path d="M -36 36 A 51 51 0 1 1 51 5" fill="none" stroke="url(#arc-grad)" stroke-width="6"/>
        <path d="M 48 9 A 49 49 0 0 1 -34 35" fill="none" stroke="#2f8fd0" stroke-width="1"/>
        <circle r="39" fill="url(#disc-grad)" filter="url(#disc-shadow)"/>
        <circle r="33" fill="none" stroke="#9ec6e6" stroke-width=".6"/>
      </g>
      <!-- generic person pictogram, origin at head centre -->
      <g id="person">
        <circle cx="0" cy="0" r="7"/>
        <path d="M-11 22 V15 Q-11 9 -5 9 H5 Q11 9 11 15 V22 Z"/>
        <path d="M-1 10 H1 V18 H-1 Z" fill="#fff"/>
      </g>
    </defs>
  </svg>

  <!-- Step 1 -->
  <div class="step-badge" style="left:156px"><svg viewBox="-60 -60 120 120" width="120" height="120"><use href="#badge"/></svg><span class="step-number">1</span></div>
  <div class="connector" style="left:158px"></div>
  <div class="step-icon" style="left:108px;width:78px">
    <svg viewBox="0 0 78 74" role="img" aria-label="Phone call icon">
      <g fill="url(#icon-grad)">
        <use href="#person" transform="translate(13 48)"/>
        <path d="M23 20 c-4 3 -4 11 3 22 c7 11 15 16 21 16 l5 -5 l-8 -8 l-5 4 c-4 -2 -10 -9 -12 -14 l4 -5 l-7 -9 z"/>
        <ellipse cx="61" cy="14" rx="16" ry="12"/>
        <path d="M50 22 L47 31 L57 25 Z"/>
      </g>
      <g fill="#fff"><circle cx="54" cy="14" r="2"/><circle cx="61" cy="14" r="2"/><circle cx="68" cy="14" r="2"/></g>
    </svg>
  </div>
  <h2 class="step-title" style="left:159px">STRONG PHONE INTERVIEW</h2>
  <span class="title-rule rule-a" style="left:154px"></span><span class="title-rule rule-b" style="left:154px"></span><span class="title-rule rule-c" style="left:154px"></span>

  <div class="divider" style="left:261px"></div>

  <!-- Step 2 -->
  <div class="step-badge" style="left:339px"><svg viewBox="-60 -60 120 120" width="120" height="120"><use href="#badge"/></svg><span class="step-number">2</span></div>
  <div class="connector" style="left:340px"></div>
  <div class="step-icon" style="left:315px;width:72px">
    <svg viewBox="0 0 72 74" role="img" aria-label="Candidate search icon">
      <g fill="url(#icon-grad)">
        <path d="M27 2 a25 25 0 1 0 0.01 0 Z M27 10 a17 17 0 1 1 -0.01 0 Z" fill-rule="evenodd"/>
        <use href="#person" transform="translate(27 20) scale(.75)"/>
      </g>
      <line x1="45" y1="46" x2="66" y2="68" stroke="url(#icon-grad)" stroke-width="9" stroke-linecap="round"/>
    </svg>
  </div>
  <h2 class="step-title" style="left:343px">PRE-EMPLOYMENT</h2>
  <span class="title-rule rule-a" style="left:342px"></span><span class="title-rule rule-b" style="left:342px"></span><span class="title-rule rule-c" style="left:342px"></span>

  <div class="divider" style="left:426px"></div>

  <!-- Step 3 -->
  <div class="step-badge" style="left:533px"><svg viewBox="-60 -60 120 120" width="120" height="120"><use href="#badge"/></svg><span class="step-number">3</span></div>
  <div class="connector" style="left:533px"></div>
  <div class="step-icon" style="left:490px;width:72px">
    <svg viewBox="0 0 72 74" role="img" aria-label="In-person meeting icon">
      <g fill="url(#icon-grad)">
        <use href="#person" transform="translate(45 10)"/>
        <path d="M2 52 L18 38 H70 L54 52 Z"/>
        <use href="#person" transform="translate(28 36) scale(1.1)"/>
      </g>
    </svg>
  </div>
  <h2 class="step-title" style="left:529px">DO IN-PERSON INTERVIEW</h2>
  <span class="title-rule rule-a" style="left:528px"></span><span class="title-rule rule-b" style="left:528px"></span><span class="title-rule rule-c" style="left:528px"></span>

  <div class="divider" style="left:626px"></div>

  <!-- Step 4 -->
  <div class="step-badge" style="left:716px"><svg viewBox="-60 -60 120 120" width="120" height="120"><use href="#badge"/></svg><span class="step-number">4</span></div>
  <div class="connector" style="left:717px"></div>
  <div class="step-icon" style="left:645px;width:148px">
    <svg viewBox="0 0 148 74" role="img" aria-label="Interview panel icon">
      <g fill="url(#icon-grad-h)">
        <use href="#person" transform="translate(37 10)"/>
        <use href="#person" transform="translate(80 10)"/>
        <use href="#person" transform="translate(116 10)"/>
        <path d="M0 52 L18 38 H148 L130 52 Z"/>
        <use href="#person" transform="translate(63 36) scale(1.1)"/>
      </g>
    </svg>
  </div>
  <h2 class="step-title" style="left:719px">SECOND INTERVIEW</h2>
  <span class="title-rule rule-a" style="left:715px"></span><span class="title-rule rule-b" style="left:715px"></span><span class="title-rule rule-c" style="left:715px"></span>

  <div class="divider" style="left:817px"></div>

  <!-- Step 5 -->
  <div class="step-badge" style="left:903px"><svg viewBox="-60 -60 120 120" width="120" height="120"><use href="#badge"/></svg><span class="step-number">5</span></div>
  <div class="connector" style="left:904px"></div>
  <div class="step-icon" style="left:872px;width:76px">
    <svg viewBox="0 0 76 74" role="img" aria-label="Document with check mark">
      <path d="M8 4 H40 L50 14 V60 H8 Z" fill="none" stroke="url(#icon-grad)" stroke-width="3.5" stroke-linejoin="round"/>
      <path d="M40 4 V14 H50 Z" fill="url(#icon-grad)"/>
      <g stroke="url(#icon-grad)" stroke-width="3" stroke-linecap="round">
        <line x1="15" y1="18" x2="30" y2="18"/><line x1="15" y1="26" x2="42" y2="26"/>
        <line x1="15" y1="34" x2="40" y2="34"/><line x1="15" y1="42" x2="32" y2="42"/><line x1="15" y1="50" x2="28" y2="50"/>
      </g>
      <circle cx="50" cy="49" r="15" fill="url(#icon-grad)"/>
      <path d="M43 49 L48 54 L57 44" fill="none" stroke="#fff" stroke-width="3.5" stroke-linecap="round" stroke-linejoin="round"/>
    </svg>
  </div>
  <h2 class="step-title" style="left:910px">REFERENCE CHECKS</h2>
  <span class="title-rule rule-a" style="left:903px"></span><span class="title-rule rule-b" style="left:903px"></span><span class="title-rule rule-c" style="left:903px"></span>

  <div class="divider" style="left:993px"></div>

  <!-- Step 6 -->
  <div class="step-badge" style="left:1086px"><svg viewBox="-60 -60 120 120" width="120" height="120"><use href="#badge"/></svg><span class="step-number">6</span></div>
  <div class="connector" style="left:1086px"></div>
  <div class="step-icon" style="left:1034px;width:98px">
    <svg viewBox="0 0 98 74" role="img" aria-label="ID card handed over icon">
      <rect x="3" y="17" width="52" height="32" rx="2" fill="none" stroke="url(#icon-grad)" stroke-width="4"/>
      <g fill="url(#icon-grad)">
        <use href="#person" transform="translate(15 26) scale(.5)"/>
        <rect x="25" y="24" width="24" height="3"/><rect x="25" y="31" width="24" height="3"/><rect x="25" y="38" width="18" height="3"/>
        <path d="M54 12 L72 30 L86 48 V62 H64 L48 44 L56 40 L52 32 Z"/>
        <rect x="88" y="46" width="9" height="20"/>
      </g>
    </svg>
  </div>
  <h2 class="step-title" style="left:1085px">JOB OFFER</h2>
  <span class="title-rule rule-a" style="left:1090px"></span><span class="title-rule rule-b" style="left:1090px"></span><span class="title-rule rule-c" style="left:1090px"></span>
</main>
</body>
</html>
```